Casino with the 'highest winning percentage' needs a stationery design

This is for a casino in Colombo, Sri Lanka and we need a stationery design for business card, letter head and envelope.

Should be very professional, simple and elegant without fancy fonts

Reason: Not fully satisfied with the designs. Need more designs.

Industry/Entity Type

Business

Requirements
Must have
• 1. card deck symbol 'CLUBS' in red, or black

2. name in BLOCK CAPITAL LETTERS

3. Preferred font colours are black, white or red

4. Prefer 'professional /elegant' fonts
Should not have
• SHOULD NOT HAVE ANY OTHER SYMBOL EXCEPT 'CLUBS'

DO NOT PREFER ITALIC FONTS

```html
<!DOCTYPE html>
<html lang="en">
<head>
<meta charset="utf-8">
<title>Veranda House – Stationery</title>
<link rel="stylesheet" href="https://fonts.googleapis.com/css2?family=Arimo:wght@400&family=Caladea:wght@400;700&display=swap">
<style>
  :root{
    --backdrop:#24262b;
    --paper:#ffffff;
    --paper-shade:#eeeeef;
    --brand-red:#d1293a;
    --ink:#1c1c1c;
    --muted:#555;
    --rule:#333;
    --box:#c9c9c9;
    --flap:#0c0c0c;
    --watermark:#f8e4e4;
  }
  *{margin:0;padding:0;box-sizing:border-box}
  html,body{width:1200px;height:497px;overflow:hidden;background:var(--backdrop)}
  body{position:relative;font-family:"Caladea",Georgia,serif;color:var(--ink)}

  .sheet{position:absolute;top:22px;width:357px;height:462px;background:var(--paper)}
  .sheet--fax{left:10px}
  .sheet--letter{left:398px;background:linear-gradient(160deg,var(--paper-shade) 0%,var(--paper) 55%,var(--paper) 100%)}
  .accent-bar{position:absolute;background:var(--brand-red)}
  .sheet .accent-bar{left:24px;top:0;width:22px;height:76px}
  .header-rule{position:absolute;left:46px;right:0;top:76px;height:1px;background:var(--rule)}

  .brand{position:absolute;text-align:right;line-height:1;text-transform:uppercase;font-weight:700}
  .brand__name{display:flex;align-items:center;justify-content:flex-end;gap:6px}
  .brand__dot{display:inline-block;border-radius:50%;background:var(--brand-red);flex:none}
  .sheet .brand{right:28px;top:24px}
  .sheet .brand__name{font-size:13px}
  .sheet .brand__dot{width:20px;height:20px}
  .sheet .brand__line{font-size:13px;margin-top:3px}
  .sheet .brand__place{font-size:7px;margin-top:2px}

  .contact-line{position:absolute;left:0;right:0;top:82px;text-align:center;font-size:6.8px;color:var(--muted)}
  .footer-address{position:absolute;right:28px;bottom:16px;font-size:6.6px;color:var(--muted)}

  .fax-title{position:absolute;left:24px;top:100px;font-family:"Arimo",Arial,sans-serif;font-size:21px;font-weight:400;line-height:1}
  .fax-field{position:absolute;left:24px;width:306px;height:12px;border-bottom:1px solid var(--rule);font-family:"Arimo",Arial,sans-serif;font-size:6.4px;line-height:1}
  .fax-field span{position:absolute;top:1px}
  .fax-field span:last-child{left:162px}
  .fax-field--to{top:130px}
  .fax-field--fax{top:149px}
  .fax-field--phone{top:168px}
  .fax-field--re{top:187px}
  .fax-options{position:absolute;left:24px;top:214px;display:flex;gap:16px;font-family:"Arimo",Arial,sans-serif;font-size:6.4px}
  .fax-options label{display:flex;align-items:center;gap:5px}
  .fax-options i{display:inline-block;width:7px;height:7px;background:var(--box)}

  .watermark{position:absolute;left:108px;top:198px;width:136px;height:136px;border-radius:50%;background:var(--watermark)}

  .card{position:absolute;width:147px;height:83px;background:var(--paper);border-radius:8px;overflow:hidden}
  .card--front{left:899px;top:6px;background:linear-gradient(170deg,var(--paper) 40%,var(--paper-shade))}
  .card--front .accent-bar{left:7px;top:0;width:15px;height:46px}
  .card--front .header-rule{left:22px;top:46px;background:#888}
  .card--front .brand{right:9px;top:8px}
  .card--front .brand__name{font-size:8px;gap:4px}
  .card--front .brand__dot{width:12px;height:12px}
  .card--front .brand__line{font-size:8px;margin-top:2px}
  .card--front .brand__place{font-size:4.5px;margin-top:1px}
  .card-details{position:absolute;left:10px;right:9px;font-size:4px;color:var(--muted);white-space:nowrap}
  .card-details--phones{top:51px}
  .card-details--online{top:62px;text-align:right;line-height:1.4}
  .card-details--address{top:74px;text-align:right}

  .card--back-a{left:814px;top:106px}
  .card--back-b{left:988px;top:106px}
  .mini-mark{position:absolute;text-align:center;text-transform:uppercase;font-weight:700;line-height:1.1;font-size:5.5px;white-space:nowrap}
  .mini-mark small{display:block;font-size:3.5px;margin-top:1px}
  .mini-mark .brand__dot{width:6px;height:6px;margin-bottom:1px}
  .mini-mark--large{font-size:7.5px}
  .mini-mark--large .brand__name{justify-content:center;gap:4px}
  .mini-mark--large .brand__dot{width:10px;height:10px;margin:0}
  .card-watermark{position:absolute;left:47px;top:14px;width:52px;height:52px;border-radius:50%;background:var(--watermark)}

  .envelope-flap{position:absolute;left:793px;top:206px;width:353px;height:47px}
  .envelope{position:absolute;left:793px;top:266px;width:353px;height:219px;background:linear-gradient(170deg,var(--paper) 40%,var(--paper-shade));border-radius:70px 70px 0 0/44px 44px 0 0;overflow:hidden}
  .envelope .seal{position:absolute;left:167px;top:16px;width:20px;height:20px;border-radius:50%;background:var(--brand-red);box-shadow:0 0 0 1px #fff,0 0 0 2px #999}
  .envelope .flap-rule{position:absolute;left:0;right:0;top:45px;height:1px;background:#9a9a9a}
  .envelope .accent-bar{left:19px;top:46px;width:22px;height:76px}
  .envelope .header-rule{left:41px;top:122px}
  .envelope .brand{left:46px;top:72px}
  .envelope .brand__name{font-size:12px;gap:6px}
  .envelope .brand__dot{width:18px;height:18px}
  .envelope .brand__line{font-size:12px;margin-top:3px}
  .envelope .brand__place{font-size:6.5px;margin-top:2px}
  .envelope-address{position:absolute;left:53px;top:126px;font-size:6.6px;line-height:1.5;color:var(--muted)}
  .envelope-web{position:absolute;left:60px;top:193px;font-size:6.6px;color:var(--muted)}
</style>
</head>
<body>

  <!-- Fax sheet -->
  <section class="sheet sheet--fax">
    <div class="accent-bar"></div>
    <div class="header-rule"></div>
    <div class="brand">
      <div class="brand__name"><i class="brand__dot"></i>Veranda House</div>
      <div class="brand__line">Gaming Lounge</div>
      <div class="brand__place">Colombo</div>
    </div>
    <p class="contact-line">t : + 94 11 2456780 | f : + 94 11 0000000 | e : info@verandahouse.lk | w : www.verandahouse.lk</p>
    <h1 class="fax-title">FAX</h1>
    <div class="fax-field fax-field--to"><span>To :</span><span>From :</span></div>
    <div class="fax-field fax-field--fax"><span>Fax :</span><span>Page:</span></div>
    <div class="fax-field fax-field--phone"><span>Phone :</span><span>Date:</span></div>
    <div class="fax-field fax-field--re"><span>Re :</span><span>CC:</span></div>
    <div class="fax-options">
      <label><i></i>Urgent</label>
      <label><i></i>For Review</label>
      <label><i></i>Please Comment</label>
      <label><i></i>Please Reply</label>
      <label><i></i>Please Recycle</label>
    </div>
    <p class="footer-address">58, Lotus Terrace, Mawatha, Colombo 01000, Sri Lanka</p>
  </section>

  <!-- Letterhead -->
  <section class="sheet sheet--letter">
    <div class="accent-bar"></div>
    <div class="header-rule"></div>
    <div class="brand">
      <div class="brand__name"><i class="brand__dot"></i>Veranda House</div>
      <div class="brand__line">Gaming Lounge</div>
      <div class="brand__place">Colombo</div>
    </div>
    <p class="contact-line">t : + 94 11 2456780 | f : + 94 11 0000000 | e : info@verandahouse.lk | w : www.verandahouse.lk</p>
    <div class="watermark"></div>
    <p class="footer-address">58, Lotus Terrace, Mawatha, Colombo 01000, Sri Lanka</p>
  </section>

  <!-- Business card front -->
  <section class="card card--front">
    <div class="accent-bar"></div>
    <div class="header-rule"></div>
    <div class="brand">
      <div class="brand__name"><i class="brand__dot"></i>Veranda House</div>
      <div class="brand__line">Gaming Lounge</div>
      <div class="brand__place">Colombo</div>
    </div>
    <p class="card-details card-details--phones">m : + 94 77 0000000 | t : + 94 11 2456780 | f : + 94 11 0000000</p>
    <p class="card-details card-details--online">e : info@verandahouse.lk<br>w : www.verandahouse.lk</p>
    <p class="card-details card-details--address">58, Lotus Terrace Mawatha, Colombo 01000, Sri Lanka</p>
  </section>

  <!-- Business card back, variant A -->
  <section class="card card--back-a">
    <div class="card-watermark"></div>
    <div class="mini-mark" style="left:10px;top:32px"><i class="brand__dot"></i><br>Veranda<br>Casino<small>Sri Lanka</small></div>
    <div class="mini-mark" style="left:52px;top:40px">Veranda<br>Gaming Lounge<small>Colombo</small></div>
    <div class="mini-mark" style="left:110px;top:40px">Veranda<br>Casino<small>Colombo</small></div>
  </section>

  <!-- Business card back, variant B -->
  <section class="card card--back-b">
    <div class="mini-mark mini-mark--large" style="left:38px;top:12px">
      <div class="brand__name"><i class="brand__dot"></i>Veranda House</div>Gaming Lounge<small>Sri Lanka</small>
    </div>
    <div class="mini-mark" style="left:13px;top:50px"><i class="brand__dot"></i><br>Veranda<br>Casino<small>Sri Lanka</small></div>
    <div class="mini-mark" style="left:50px;top:58px">Veranda<br>Gaming Lounge<small>Colombo</small></div>
    <div class="mini-mark" style="left:110px;top:58px">Veranda<br>Casino<small>Colombo</small></div>
  </section>

  <!-- Envelope flap (back) -->
  <svg class="envelope-flap" viewBox="0 0 353 47" aria-hidden="true">
    <path d="M0 47 L22 12 Q30 0 60 0 L293 0 Q323 0 331 12 L353 47 Z" fill="var(--flap)"/>
    <circle cx="176.5" cy="24" r="10" fill="var(--brand-red)" stroke="#fff" stroke-width="1"/>
  </svg>

  <!-- Envelope front -->
  <section class="envelope">
    <div class="seal"></div>
    <div class="flap-rule"></div>
    <div class="accent-bar"></div>
    <div class="header-rule"></div>
    <div class="brand">
      <div class="brand__name"><i class="brand__dot"></i>Veranda House</div>
      <div class="brand__line">Gaming Lounge</div>
      <div class="brand__place">Colombo</div>
    </div>
    <p class="envelope-address">58, Lotus TerraceMawatha<br>Colombo 01000, Sri Lanka</p>
    <p class="envelope-web">www.verandahouse.lk</p>
  </section>

</body>
</html>
```